Web Design Project - Event Management Company

A web-page design needs to be created for an event management company. The logo has already been created, the design needs to draw on the themes and colors of the logo and extend on that.

The event management company likes to differentiate itself from others by being a bit "un-conventional" and being able to think outside the box.

the specialise in corporate events, weddings, AGMs, anything that requires coordination of resources. They also can provide Audio Visual services such as recording events.

final design will also require HTML implementation

```html
<!DOCTYPE html>
<html lang="en">
<head>
<meta charset="utf-8">
<title>Odd Block Group – Event Management</title>
<link href="https://fonts.googleapis.com/css2?family=Cabin:wght@400;500;600;700&family=Open+Sans:ital,wght@0,400;0,600;0,700;1,400;1,600&family=Arimo:wght@400&display=swap" rel="stylesheet">
<style>
:root{
  --orange-light:#f5a236;
  --orange:#ef7a22;
  --orange-deep:#e85a24;
  --ink:#333333;
  --ink-soft:#444444;
  --panel:#f4f2f2;
  --panel-line:#e2dede;
  --nav-active:#3a3a3a;
  --footer-top:#4a4a4a;
  --footer-bottom:#2a2a2a;
  --white:#ffffff;
  --link:#e8602a;
}
*{margin:0;padding:0;box-sizing:border-box}
html,body{width:1045px;height:1200px;overflow:hidden}
body{position:relative;background:var(--white);font-family:"Open Sans",sans-serif;color:var(--ink)}
.header-backdrop{position:absolute;left:0;top:0;width:1045px;height:568px;
  background:radial-gradient(ellipse at 95% 20%,#e9e9e9 0%,#f3f3f3 35%,#ffffff 70%)}
.brand{position:absolute;left:98px;top:84px;display:flex;align-items:center;gap:8px}
.brand-mark{width:22px;height:22px;background:var(--orange)}
.brand-name{font-family:"Cabin",sans-serif;font-weight:600;font-size:25px;color:var(--ink-soft);letter-spacing:.5px}
.phone{position:absolute;right:91px;top:10px;font-family:"Cabin",sans-serif;font-size:25px;color:var(--ink-soft)}
.social{position:absolute;top:78px;left:792px;display:flex;gap:8px}
.social span{width:32px;height:32px;border-radius:50%;background:#c9c9c9;border:2px solid #ffffff;box-shadow:0 1px 3px rgba(0,0,0,.25)}
.nav{position:absolute;left:90px;top:121px;width:867px;height:40px;border-radius:6px;
  background:linear-gradient(#f5a03a,#ec6a22);display:flex;align-items:center;padding-left:21px}
.nav a{font-family:"Cabin",sans-serif;font-size:12.5px;color:var(--white);text-decoration:none;text-transform:uppercase;height:40px;line-height:40px}
.nav a.active{background:var(--nav-active);width:61px;text-align:center}
.nav a+a{margin-left:50px}
.hero{position:absolute;left:90px;top:175px;width:866px;height:341px;background:var(--white);
  border:1px solid #e4e4e4;box-shadow:0 14px 14px -10px rgba(0,0,0,.18)}
.hero-photo{position:absolute;left:8px;top:8px;width:849px;height:325px;
  background:linear-gradient(180deg,#6a5a48 0%,#b39a6e 35%,#5b4a5a 65%,#9a7fc4 85%,#3d3040 100%)}
.welcome-band{position:absolute;left:0;top:568px;width:1045px;height:204px;
  background:linear-gradient(180deg,var(--orange-light),var(--orange-deep))}
.welcome-photo-frame{position:absolute;left:90px;top:22px;width:236px;height:171px;background:var(--white);padding:5px}
.welcome-photo{width:100%;height:100%;background:linear-gradient(135deg,#3a2410,#b98a3a 45%,#f0d48a 60%,#5a3a18)}
.welcome-title{position:absolute;left:335px;top:12px;font-family:"Cabin",sans-serif;font-weight:700;font-size:42px;color:var(--white);letter-spacing:1px}
.welcome-text{position:absolute;left:338px;top:72px;width:297px;font-size:9.5px;line-height:14px;color:var(--white);text-align:justify}
.testimonials{position:absolute;left:656px;top:0;width:389px;height:204px;
  background:linear-gradient(90deg,rgba(170,80,20,.25),rgba(0,0,0,0) 12%)}
.testimonials h2{position:absolute;left:38px;top:8px;font-family:"Cabin",sans-serif;font-weight:600;font-size:23px;color:var(--white)}
.testimonials p{position:absolute;left:38px;top:54px;width:272px;font-family:"Arimo",sans-serif;font-size:12.2px;line-height:21px;color:var(--white)}
.quote{font-family:"Cabin",sans-serif;font-style:italic;font-size:26px;color:var(--white);line-height:0}
.quote-open{position:absolute;left:20px;top:58px}
.quote-close{position:relative;top:8px;margin-left:2px}
.card{position:absolute;top:798px;width:260px;height:329px;background:var(--panel);border:1px solid var(--panel-line);box-shadow:0 0 3px rgba(0,0,0,.08)}
.card-event{left:100px}
.card-ent{left:398px}
.card-latest{left:689px}
.card-title{position:absolute;left:14px;top:14px;display:flex;align-items:center;gap:8px;font-family:"Cabin",sans-serif;font-size:20px;color:var(--ink)}
.card-title i{width:27px;height:27px;background:var(--orange);display:block}
.card-photo-frame{position:absolute;left:9px;top:54px;width:240px;height:168px;background:var(--white);padding:6px}
.card-ent .card-photo-frame{top:58px;height:163px;padding:6px 8px}
.card-photo{width:100%;height:100%}
.photo-table{background:linear-gradient(120deg,#f6f3ef 0%,#e8e2da 40%,#b52020 55%,#f2eeea 75%,#c8b6a0 100%)}
.photo-crowd{background:radial-gradient(ellipse at 50% 35%,#f2c81a 0%,#c07a10 45%,#1a1005 90%)}
.card-text{position:absolute;left:13px;top:240px;width:235px;font-size:9.6px;line-height:15.7px;text-align:justify;color:var(--ink)}
.card-text em{font-weight:600}
.more{position:absolute;font-size:9px;font-weight:700;color:var(--link);text-decoration:underline;white-space:nowrap}
.card-event .more{right:16px;top:309px}
.card-ent .more{right:24px;top:305px}
.event-item{position:absolute;left:10px;width:238px;height:80px}
.event-thumb{position:absolute;left:0;top:0;width:38px;height:38px}
.thumb-a{background:linear-gradient(#6a2010,#c84030)}
.thumb-b{background:linear-gradient(#1a1a3a,#c83030 55%,#101020)}
.thumb-c{background:linear-gradient(#e8dcb8,#b89a60)}
.event-item h3{position:absolute;left:47px;top:-4px;font-size:11px;font-weight:600;color:#111;white-space:nowrap}
.event-item p{position:absolute;left:47px;top:12px;width:192px;font-size:9.6px;line-height:14px;color:var(--ink)}
.event-meta{position:absolute;left:8px;top:52px;font-size:9.6px;font-style:italic;color:var(--ink)}
.event-item .more{left:195px;top:53px}
.footer{position:absolute;left:0;top:1151px;width:1045px;height:49px;background:linear-gradient(var(--footer-top),var(--footer-bottom));
  font-family:"Arimo",sans-serif;font-size:11.5px;color:var(--white);padding-top:16px;text-align:center;padding-right:105px}
</style>
</head>
<body>
<div class="header-backdrop" role="img" aria-label="Soft grey floral background pattern"></div>

<div class="brand"><span class="brand-mark"></span><span class="brand-name">ODD BLOCK GROUP</span></div>
<div class="phone">Call (000 1234 5678)</div>
<div class="social" aria-label="Social links"><span></span><span></span><span></span><span></span></div>

<nav class="nav">
  <a class="active" href="#">Home</a>
  <a href="#">About Us</a>
  <a href="#">Corporate</a>
  <a href="#">Social</a>
  <a href="#">Weddings</a>
  <a href="#">Portfolio</a>
  <a href="#">Contact Us</a>
</nav>

<div class="hero">
  <div class="hero-photo" role="img" aria-label="Grand ballroom set with round banquet tables under purple and gold stage lights"></div>
</div>

<section class="welcome-band">
  <div class="welcome-photo-frame"><div class="welcome-photo" role="img" aria-label="Champagne glasses glowing in warm candlelight"></div></div>
  <h1 class="welcome-title">Welcome</h1>
  <p class="welcome-text">Lorem Ipsum is simply dummy text of the printing and typesetting industry. Lorem Ipsum has been the industry's standard dummy text ever since the 1500s, when an unknown printer took a galley of type and scrambled it to make a type specimen book. It has survived not only five centuries, but also the leap into electronic typesetting, remaining essentially unchanged. It was popularised in the 1960s with the release of Letraset sheets containing Lorem Ipsum passages, and more recently.........</p>
  <div class="testimonials">
    <h2>Testimonials</h2>
    <span class="quote quote-open">“</span>
    <p>Lorem Ipsum is simply dummy text of the printing and typesetting industry. Lorem Ipsum has been the industry's standard dummy text ever since the 1500s, when an unknown printer took a galley of type and scrambled it to make a type specimen book......<span class="quote quote-close">”</span></p>
  </div>
</section>

<article class="card card-event">
  <div class="card-title"><i></i>Event Management</div>
  <div class="card-photo-frame"><div class="card-photo photo-table" role="img" aria-label="Banquet table with red folded napkins and glassware"></div></div>
  <p class="card-text"><em>Lorem Ipsum is simply dummy text of the printing and typesetting industry.</em> Lorem Ipsum has been the industry's standard dummy text ever since the 1500s, when an unknown printer.......</p>
  <a class="more" href="#">details...</a>
</article>

<article class="card card-ent">
  <div class="card-title"><i></i>Entertainment</div>
  <div class="card-photo-frame"><div class="card-photo photo-crowd" role="img" aria-label="Concert crowd silhouetted against golden stage light"></div></div>
  <p class="card-text"><em>Lorem Ipsum is simply dummy text of the printing and typesetting industry.</em> Lorem Ipsum has been the industry's standard dummy text ever since the 1500s, when an unknown printer.......</p>
  <a class="more" href="#">details...</a>
</article>

<article class="card card-latest">
  <div class="card-title"><i></i>Latest Events</div>
  <div class="event-item" style="top:64px">
    <div class="event-thumb thumb-a" role="img" aria-label="Stage event thumbnail"></div>
    <h3>Tellus justo sollicitudin</h3>
    <p>Ut felis. Dui amet, elit nulla tristique dolor, cras luctus. Nulla aliquam, adipiscing....</p>
    <span class="event-meta">Posted by : Lena Hart</span>
    <a class="more" href="#">details...</a>
  </div>
  <div class="event-item" style="top:155px">
    <div class="event-thumb thumb-b" role="img" aria-label="Concert stage thumbnail"></div>
    <h3>Tellus justo sollicitudin</h3>
    <p>Ut felis. Dui amet, elit nulla tristique dolor, cras luctus. Nulla aliquam, adipiscing....</p>
    <span class="event-meta">Posted by : Lena Hart</span>
    <a class="more" href="#">details...</a>
  </div>
  <div class="event-item" style="top:245px">
    <div class="event-thumb thumb-c" role="img" aria-label="Wedding venue thumbnail"></div>
    <h3>Tellus justo sollicitudin</h3>
    <p>Ut felis. Dui amet, elit nulla tristique dolor, cras luctus. Nulla aliquam, adipiscing....</p>
    <span class="event-meta">Posted by : Lena Hart</span>
    <a class="more" href="#">details...</a>
  </div>
</article>

<footer class="footer">Copyright © Odd block group | Legal | Sitemap</footer>
</body>
</html>
```